Natural Organic soap need packaging design

we need a packaging design for new company based in New Zealand Called 'Tellum Global ltd'.. We manufacture Natural organic soap bars.our main USP is that this soap is made of all natural ingredient and no chemical used and soap is made in New Zealand,so we need a design which look natural,simple,classy and luxury and packaging should reflect that its made in New Zealand.please find attached photos of sample soap.
soap will be in two variant:
1. Pure Manuka Honey soap
2. Goat Milk soap
NOTE: the soap in picture is not actually our soap its just a sample what our soap will look like so please don't make a design with FRAKKK written on it. TELLUM is the soap name.
Target Market(s)
international market. mainly young and kids
Industry/Entity Type
It Company
Look and feel

```html
<!DOCTYPE html>
<html lang="en">
<head>
<meta charset="utf-8">
<title>Tellum Goat Milk Soap – Packaging</title>
<link rel="stylesheet" href="https://fonts.googleapis.com/css2?family=Open+Sans:wght@400;600&display=swap">
<style>
  :root {
    --backdrop: #e4e4e4;
    --carton-red: #8e1820;
    --carton-red-deep: #7a131a;
    --carton-blue: #232d6e;
    --carton-blue-deep: #1b2459;
    --silver: #d9d9d9;
    --frame-line: #f1e9e9;
  }
  * { box-sizing: border-box; margin: 0; padding: 0; }
  html, body { width: 1200px; height: 801px; overflow: hidden; }
  body {
    background: var(--backdrop);
    font-family: "Open Sans", sans-serif;
    position: relative;
  }
  .panel { position: absolute; overflow: hidden; }
  .panel--front {
    left: 248px; top: 200px; width: 314px; height: 490px;
    background: var(--carton-red);
  }
  .panel--side {
    left: 765px; top: 178px; width: 155px; height: 532px;
    background: var(--carton-blue);
  }
  .panel__frame { position: absolute; inset: 0; }
  .star-field {
    position: absolute;
    border-radius: 50%;
    opacity: 0.55;
  }
  .panel--front .star-field {
    left: 120px; top: 40px; width: 150px; height: 330px;
    background: radial-gradient(closest-side, var(--carton-red-deep), transparent);
  }
  .panel--side .star-field {
    left: 20px; top: 20px; width: 120px; height: 420px;
    background: radial-gradient(closest-side, var(--carton-blue-deep), transparent);
  }
  .label {
    position: absolute;
    left: 50%; top: 50%;
    transform: translate(-50%, -50%) rotate(-90deg);
    color: var(--silver);
    display: flex;
  }
  .panel--front .label {
    width: 490px; height: 314px;
    flex-direction: column; align-items: center; justify-content: center;
  }
  .panel--side .label {
    width: 532px; height: 155px;
    flex-direction: row; align-items: center; justify-content: center; gap: 44px;
  }
  .product-name {
    font-weight: 400; color: #fff; white-space: nowrap;
  }
  .panel--front .product-name { font-size: 25px; margin-bottom: 2px; }
  .panel--side .product-name { font-size: 23px; order: 2; margin-top: -22px; }
  .brand { display: flex; flex-direction: column; align-items: center; }
  .brand__name {
    font-weight: 600; line-height: 1; letter-spacing: 2px; color: var(--silver);
  }
  .panel--front .brand__name { font-size: 84px; }
  .panel--side .brand__name { font-size: 48px; }
  .brand__origin {
    font-weight: 400; color: var(--silver); letter-spacing: 10px; white-space: nowrap;
  }
  .panel--front .brand__origin { font-size: 12px; margin-top: 12px; }
  .panel--side .brand__origin { font-size: 10px; letter-spacing: 8px; margin-top: 8px; }
  .panel--side .brand { order: 1; }
</style>
</head>
<body>
  <section class="panel panel--front" aria-label="Front of carton">
    <div class="star-field" role="img" aria-label="Faint Southern Cross star decoration"></div>
    <svg class="panel__frame" width="314" height="490" viewBox="0 0 314 490" aria-hidden="true">
      <path d="M26 12 H288 V26 H302 V464 H288 V478 H26 V464 H12 V26 H26 Z"
            fill="none" stroke="var(--frame-line)" stroke-width="2"/>
      <path d="M36 21 A12 12 0 0 1 24 33 V457 A12 12 0 0 1 36 469 H278 A12 12 0 0 1 290 457 V33 A12 12 0 0 1 278 21 Z"
            fill="none" stroke="var(--frame-line)" stroke-width="1.5"/>
    </svg>
    <div class="label">
      <p class="product-name">Goat Milk soap</p>
      <div class="brand">
        <span class="brand__name">TELLUM</span>
        <span class="brand__origin">NEW ZEALAND</span>
      </div>
    </div>
  </section>

  <section class="panel panel--side" aria-label="Side of carton">
    <div class="star-field" role="img" aria-label="Faint Southern Cross star decoration"></div>
    <div class="label">
      <p class="product-name">Goat Milk soap</p>
      <div class="brand">
        <span class="brand__name">TELLUM</span>
        <span class="brand__origin">NEW ZEALAND</span>
      </div>
    </div>
  </section>
</body>
</html>
```